Business card design for global fintech startup

Veltrix is a modern payments platform for the global insurance industry, serving international health, life, and travel insurers, MGAs, brokers, and partners.

We need a professional, premium business card for use at insurance conferences and executive meetings. The goal is to create a card that feels trustworthy, modern, and high-quality, while still being distinctive and memorable in a stack of business cards.

Target audience:
Senior insurance executives (VP, C-suite).

Design goals:
Clear, professional, and credible
Modern but not trendy
Premium and well-structured
Easy to read and practical for networking

Brand direction:
Brand-first (company over individual)
Follow existing brand guidelines where possible
Clean layout, strong hierarchy, excellent readability

Must include:
Name
Title
Company name (Veltrix)
Logo
Email
Phone/Whatsapp
Website (www.withveltrix.example)
Tagline - Confidence that carries value

Materials & finish:
Open to designer recommendations for premium look and feel.

Please avoid:
Flashy or trendy startup styles
Generic insurance icons or clichés
Cluttered layouts or hard-to-read text

Deliverables:
Front and back business card, print-ready files.

Target Market(s)

Global Insurance executives

Industry/Entity Type

Fintech, Insurtech, Insurance, Financial Services

Contact Information for Business Card

Name Title Company name (Veltrix) Logo Email Phone/Whatsapp Website (www.withveltrix.example) Tagline - Confidence that carries value

Font styles to use
Other font styles liked:
• See brand guidelines

Requirements
Nice to have
• something that stands out/makes us more memorable while still remaining professional
Should not have
• Please avoid: Flashy or trendy startup styles Generic insurance icons or clichés Cluttered layouts or hard-to-read text

```html
<!DOCTYPE html>
<html lang="en">
<head>
<meta charset="utf-8">
<title>Veltrix Business Card</title>
<link rel="stylesheet" href="https://fonts.googleapis.com/css2?family=Montserrat:wght@400;500;700&display=swap">
<style>
  :root {
    --page: #2b2b2b;
    --card: #000000;
    --white: #ffffff;
    --tagline: #3a8fd6;
    --yellow: #f7c35f;
    --orange: #f07c22;
    --sky: #44c6ea;
    --soft: #d9d9d9;
  }
  * { margin: 0; padding: 0; box-sizing: border-box; }
  html, body { width: 1200px; height: 875px; overflow: hidden; }
  body {
    background: var(--page);
    font-family: "Montserrat", Arial, sans-serif;
    color: var(--white);
    position: relative;
  }
  .card {
    position: absolute;
    width: 540px;
    height: 310px;
    background: var(--card);
    border-radius: 22px;
    top: 282px;
  }
  .card-back { left: 40px; }
  .card-front { left: 620px; }

  .brand {
    position: absolute;
    display: flex;
    align-items: center;
    gap: 16px;
  }
  .card-back .brand {
    left: 50%;
    top: 50%;
    transform: translate(-50%, -50%);
  }
  .brand-dot {
    width: 30px;
    height: 30px;
    border-radius: 50%;
    background: var(--tagline);
  }
  .brand-name {
    font-weight: 500;
    font-size: 44px;
    letter-spacing: 6px;
    text-transform: uppercase;
    line-height: 1;
  }

  .card-front .brand { left: 38px; top: 92px; }
  .card-front .brand-name { font-size: 48px; }
  .tagline {
    position: absolute;
    left: 40px;
    top: 148px;
    font-size: 15px;
    color: var(--tagline);
    letter-spacing: 0.5px;
  }

  .person {
    position: absolute;
    right: 34px;
    top: 30px;
    text-align: right;
  }
  .person-name { font-weight: 700; font-size: 20px; }
  .person-title { font-size: 11px; margin-top: 2px; color: var(--soft); }

  .contact {
    position: absolute;
    left: 40px;
    bottom: 24px;
    font-size: 11.5px;
    line-height: 1.45;
    list-style: none;
  }
  .contact li { display: flex; align-items: center; gap: 8px; }
  .contact .address { padding-left: 22px; margin-bottom: 2px; }
  .contact svg { width: 14px; height: 14px; flex: none; }
</style>
</head>
<body>
  <section class="card card-back" aria-label="Card back">
    <div class="brand">
      <span class="brand-dot"></span>
      <span class="brand-name">Veltrix</span>
    </div>
  </section>

  <section class="card card-front" aria-label="Card front">
    <div class="person">
      <div class="person-name">Daniel Moreau</div>
      <div class="person-title">Managing Director</div>
    </div>

    <div class="brand">
      <span class="brand-name">Veltrix</span>
    </div>
    <div class="tagline">Confidence that carries value</div>

    <ul class="contact">
      <li class="address">48 Harbour Lane,<br>Northfield, USA</li>
      <li>
        <svg viewBox="0 0 16 16" aria-hidden="true"><path fill="var(--yellow)" d="M3 2h3l1.5 3.5-2 1.3a8 8 0 0 0 3.7 3.7l1.3-2L14 10v3a1 1 0 0 1-1 1A11 11 0 0 1 2 3a1 1 0 0 1 1-1z"/></svg>
        (08) 4410 2036
      </li>
      <li>
        <svg viewBox="0 0 16 16" aria-hidden="true"><rect x="1" y="3" width="14" height="10" rx="1" fill="var(--orange)"/><path d="M1.5 3.5 8 9l6.5-5.5" fill="none" stroke="#000" stroke-width="1.2"/></svg>
        hello@veltrix.example
      </li>
      <li>
        <svg viewBox="0 0 16 16" aria-hidden="true"><circle cx="8" cy="8" r="6.5" fill="none" stroke="var(--sky)" stroke-width="1.5"/><ellipse cx="8" cy="8" rx="2.8" ry="6.5" fill="none" stroke="var(--sky)" stroke-width="1.2"/><path d="M1.5 8h13" stroke="var(--sky)" stroke-width="1.2"/></svg>
        www.withveltrix.example
      </li>
    </ul>
  </section>
</body>
</html>
```